Broschüre für Nachlassverwaltung und Testamentsvollstreckung
Zielgruppe
Nachlassverwaltung und Testamentsvollstreckung
Aufgabenstellung
Ich brauche:
1. ) Präsentationsmappe: mit Visitenkartentasche innenliegend links unten, Endformat: 440 x 307 mm
Endformat: 440 x 307 mm
Seitenanzahl: 2-seitig
Farbigkeit: 4/4-farbig
Diese Beschreibung bezieht sich auf unsere Topseller-Sorte 0,40 mm starker Chromokarton 255g (zertifiziert mit KWRB-Siegel für Nachhaltigkeit), hohe Steifigkeit mit 1,6-fachem Volumen. Weitere Sorten finden Sie in der Produktauswahl.
Hochwertige Mappe für DIN A4, 4/4 farbig (Außen- und Innenseite bedruckt)
0,40 mm starker Chromokarton 255g (zertifiziert mit KWRB-Siegel für Nachhaltigkeit), hohe Steifigkeit mit 1,6-fachem Volumen
Datenformat: 45,0 x 31,7 cm
Endformat: 44,0 x 30,7 cm
2. ) Ringordner
Ringbuch (2-Loch) bis zu 400 DIN A4 Blätter
Außen- und Innenseite farbig bedruckt (4/4)
Hochwertiger Qualitätsdruck mit Glanzfolie veredelt
4/4 farbig außen und innen
Endformat: 61,5 cm x 31,5 cm
geschlossenes Endformat: 28,2 cm x 31,5 cm
Datenformat: 65,1 cm x 35,1 cm
Folgende Dienstleistungen sollten mit aufgeführt sein:
- Testamentsvollstreckung
- Nachlassabwicklung
- Nachlassverwaltung
- Nachlasspflege

```html
<!DOCTYPE html>
<html lang="de">
<head>
<meta charset="utf-8">
<title>Varel Nachlassmanagement – Ringordner</title>
<link rel="stylesheet" href="https://fonts.googleapis.com/css2?family=Playfair+Display:ital,wght@0,600;1,700&family=Montserrat:wght@400;500&family=Questrial&display=swap">
<style>
:root{
  --bg-light:#ececec;
  --bg-dark:#b4b4b4;
  --ink:#3a3a3a;
  --band:#1f1f1f;
  --cream:#f3ece2;
  --cream-mist:#e7e2d8;
  --teal:#2f5a5e;
  --teal-deep:#173c40;
  --taupe:#9c9384;
  --on-dark:#e9e4dc;
  --muted:#6a6358;
}
*{box-sizing:border-box;margin:0;padding:0}
html,body{width:1200px;height:1200px;overflow:hidden}
body{position:relative;background:linear-gradient(160deg,var(--bg-dark),var(--bg-light) 80%);font-family:"Montserrat",sans-serif;color:var(--ink)}
.abs{position:absolute}

/* wordmark: plain name in the body font, one circle beside it */
.wordmark{position:absolute;display:flex;align-items:center;white-space:nowrap}
.wordmark .dot{flex:none;border-radius:50%;background:currentColor}
.wordmark .name{font-family:"Montserrat",sans-serif;font-weight:500;letter-spacing:.04em}
.wordmark.on-dark{color:var(--on-dark)}

.header-mark{left:50px;top:38px;color:var(--ink)}
.header-mark .dot{width:60px;height:60px}
.header-mark .name{font-size:28px;margin-left:26px}

/* cover */
.cover{left:56px;top:124px;width:485px;height:562px;overflow:hidden;border-radius:2px}
.scene{position:absolute;inset:0;background:
  linear-gradient(180deg,var(--cream-mist) 0%,var(--cream) 45%,#b9c4c0 62%,var(--teal) 82%,var(--teal-deep) 100%)}
.band{position:absolute;left:0;right:0;bottom:0;background:var(--band)}
.cover .band{height:58px}
.cover .wordmark{left:50%;top:50%;transform:translate(-50%,-50%)}
.cover .wordmark .dot{width:26px;height:26px}
.cover .wordmark .name{font-size:14px;margin-left:14px}

/* spine */
.spine{left:840px;top:124px;width:96px;height:562px;background:linear-gradient(180deg,var(--cream-mist),var(--cream));overflow:hidden}
.spine .band{height:76px}
.spine .wordmark{left:32px;top:22px}
.spine .wordmark .dot{width:32px;height:32px}
.v-text{position:absolute;writing-mode:vertical-rl;transform:rotate(180deg);font-family:"Playfair Display",serif;font-style:italic;font-weight:700;color:#3b3b3b;white-space:nowrap}
.spine .v-text{font-size:15px}
.v-small{font-size:7.5px;font-style:normal;font-weight:600}

.label{left:0;width:1200px;top:722px;text-align:center;font-family:"Questrial",sans-serif;font-size:38px;color:#1e1e1e}

/* outer spread */
.spread-out{left:39px;top:805px;width:554px;height:283px;background:var(--cream);box-shadow:0 6px 10px rgba(0,0,0,.25);overflow:hidden}
.back-photo{position:absolute;left:0;top:0;width:260px;height:105px;background:linear-gradient(180deg,#ddd6ca,rgba(243,236,226,0))}
.services{position:absolute;left:30px;top:107px;list-style:none;font-family:"Playfair Display",serif;font-weight:600;font-size:8px;color:#3d3d3d}
.services li{margin-bottom:11.5px}
.services li::before{content:"• "}
.badge{position:absolute;left:156px;top:125px;width:36px;height:45px;border-radius:4px;background:linear-gradient(160deg,#e6e6e6,#a9a9a9);border:1px solid #8a8a8a}
.contact{position:absolute;left:31px;top:196px;font-size:4.4px;line-height:1.35;color:#444}
.contact p{margin-bottom:5px}
.out-spine{position:absolute;left:261px;top:0;width:46px;height:253px}
.out-front{position:absolute;left:307px;top:0;width:247px;height:253px;background:linear-gradient(180deg,var(--cream-mist) 0%,var(--cream) 45%,#b9c4c0 63%,var(--teal) 82%,var(--teal-deep) 100%)}
.spread-out .band{height:30px}
.mini .dot{width:14px;height:14px}
.mini .name{font-size:6.5px;margin-left:8px}

/* inner spread */
.spread-in{left:620px;top:805px;width:556px;height:283px;background:linear-gradient(90deg,#faf7f2 0%,#efe9df 30%,#c9c1b4 70%,var(--taupe) 100%);box-shadow:0 6px 10px rgba(0,0,0,.25);overflow:hidden}
.portrait{position:absolute;left:27px;top:22px;width:92px;height:122px;background:linear-gradient(180deg,#d9d9d9,#8d8d8d 60%,#3a3a3a)}
.person{position:absolute;left:26px;top:150px;font-family:"Playfair Display",serif;font-weight:600;font-size:9px;color:#3a3a3a}
.bio-left{position:absolute;left:26px;top:167px;width:95px;font-size:4.2px;line-height:1.3;color:#3a3a3a}
.bio{position:absolute;left:124px;top:22px;width:86px;font-size:4.2px;line-height:1.3;color:#3a3a3a}
.bio p{margin-bottom:5px}
.member{position:absolute}
.spread-in .wordmark{left:360px;top:257px;color:var(--muted)}
</style>
</head>
<body>

<div class="wordmark header-mark"><span class="dot"></span><span class="name">VAREL NACHLASSMANAGEMENT</span></div>

<!-- binder front cover -->
<section class="abs cover">
  <div class="scene" role="img" aria-label="Foto: Mann im Anzug steigt eine lichte Treppe in Petrol-Tönen hinauf"></div>
  <div class="band">
    <div class="wordmark on-dark"><span class="dot"></span><span class="name">VAREL NACHLASSMANAGEMENT</span></div>
  </div>
</section>

<!-- binder spine -->
<section class="abs spine">
  <div class="v-text" style="left:22px;top:60px">• Nachlassverwaltung</div>
  <div class="v-text" style="left:56px;top:110px">• Nachlasspflege</div>
  <div class="v-text" style="left:22px;top:268px">• Testamentsvollstreckung</div>
  <div class="v-text" style="left:56px;top:310px">• Nachlassabwicklung</div>
  <div class="band">
    <div class="wordmark on-dark"><span class="dot"></span></div>
  </div>
</section>

<div class="abs label">Ringordner</div>

<!-- outer spread -->
<section class="abs spread-out">
  <div class="back-photo" role="img" aria-label="Blasses Foto: Richterhammer und Waage auf einem Schreibtisch"></div>
  <ul class="services">
    <li>Testamentsvollstreckung</li>
    <li>Nachlassabwicklung</li>
    <li>Nachlassverwaltung</li>
    <li>Nachlasspflege</li>
  </ul>
  <div class="badge" aria-label="Auszeichnungssiegel"></div>
  <div class="contact">
    <p>Nachlassmanagement<br>Marlene Hofstede</p>
    <p>Lindenallee 24<br>48151 Musterstadt</p>
    <p>Mail: info@varel-nachlass.de</p>
    <p>Tel.: +49 (0) 4711 / 22 30 10<br>Fax: +49 (0) 4711 / 22 30 11</p>
  </div>
  <div class="out-spine">
    <div class="v-text v-small" style="left:6px;top:20px">• Nachlassverwaltung</div>
    <div class="v-text v-small" style="left:26px;top:42px">• Nachlasspflege</div>
    <div class="v-text v-small" style="left:6px;top:128px">• Testamentsvollstreckung</div>
    <div class="v-text v-small" style="left:26px;top:144px">• Nachlassabwicklung</div>
  </div>
  <div class="out-front" role="img" aria-label="Foto: Mann im Anzug steigt eine lichte Treppe hinauf"></div>
  <div class="band">
    <div class="wordmark on-dark mini" style="left:31px;top:8px"><span class="dot"></span><span class="name">VAREL NACHLASSMANAGEMENT</span></div>
    <div class="wordmark on-dark mini" style="left:277px;top:8px"><span class="dot"></span></div>
    <div class="wordmark on-dark mini" style="left:364px;top:8px"><span class="dot"></span><span class="name">VAREL NACHLASSMANAGEMENT</span></div>
  </div>
</section>

<!-- inner spread -->
<section class="abs spread-in">
  <div class="portrait" role="img" aria-label="Schwarzweiß-Porträtfoto der Inhaberin"></div>
  <div class="person">Marlene Hofstede</div>
  <p class="bio-left">Ich bin seit vielen Jahren selbstständig tätig und begleite Angehörige, Kanzleien und Erben verlässlich bei allen Fragen rund um den Nachlass.</p>
  <div class="bio">
    <p>Bis heute widme ich mich mit großer Sorgfalt und viel Herz der Testamentsvollstreckung und Nachlassabwicklung.</p>
    <p>Ich bin geprüfte Testamentsvollstreckerin und zertifizierte Nachlasspflegerin. Durch aktive Mitgliedschaften in Fachverbänden und jährliche Lehrgänge halte ich mich stets auf dem neuesten Stand im Erb- und Nachlassrecht.</p>
    <p>In den letzten Jahren habe ich ein Netzwerk aus Steuerberatern, Rechtsanwälten, Notaren und weiteren Dienstleistern aufgebaut, um Ihnen eine schnelle und sorgenfreie Abwicklung anzubieten.</p>
    <p>Gerne übernehme ich auch die Nachlassabwicklung oder Testamentsvollstreckung für gemeinnützige Organisationen oder Privatpersonen.</p>
    <p>Ich würde mich freuen, Sie begleiten zu dürfen!</p>
  </div>
  <div class="member" style="left:133px;top:244px;width:50px;height:8px;border-radius:4px;background:#5f6fb0" aria-label="Verbandssiegel"></div>
  <div class="member" style="left:133px;top:262px;width:18px;height:18px;border-radius:50%;background:#8f9ccc" aria-label="Verbandssiegel"></div>
  <div class="member" style="left:168px;top:265px;width:38px;height:13px;background:#111" aria-label="Verbandssiegel"></div>
  <div class="wordmark mini"><span class="dot"></span><span class="name">VAREL NACHLASSMANAGEMENT</span></div>
</section>

</body>
</html>
```